Peach Point of Sale Cards for Grocery Retail Markets

We are looking to update our peach point of sale card and price card. The cards will need to be 7" x 11" with a .125 bleed - one sided. See attached for the old versions. We would like this to use photos that look like true Washington State Peaches. Here are the bullet points we would like to use: - New Crop!- Tree Ripened- Excellent FlavorNOTE: The price card just needs to have a space where a retailer can write in the sale price of the item. See attachment with the white box.

Target Market(s)

Retail market shoppers

Requirements
Must have
• Pictures of Peaches Only

```html
<!DOCTYPE html>
<html lang="en">
<head>
<meta charset="utf-8">
<title>Peach Point of Sale Cards</title>
<link rel="stylesheet" href="https://fonts.googleapis.com/css2?family=Cinzel:wght@900&family=Montserrat:wght@700;800&family=Yellowtail&display=swap">
<style>
  :root {
    --page: #f1f1f1;
    --frame: #f5a21b;
    --banner-red: #c8242b;
    --leaf-green: #17703a;
    --script-red: #c8242b;
    --accent-orange: #f0a020;
    --panel-light: #f4f4f4;
    --panel-shade: #e4e4e4;
    --fruit-gold: #f6c760;
    --fruit-red: #d8352c;
    --white: #ffffff;
  }
  html, body {
    margin: 0;
    padding: 0;
    width: 953px;
    height: 1200px;
    overflow: hidden;
    background: var(--page);
  }
  .sheet {
    position: relative;
    width: 953px;
    height: 1200px;
  }
  .pos-card {
    position: absolute;
    left: 150px;
    width: 654px;
    height: 418px;
    background: var(--frame);
  }
  .pos-card--promo { top: 119px; }
  .pos-card--price { top: 721px; }
  .card-face {
    position: absolute;
    inset: 12px;
    overflow: hidden;
    background: linear-gradient(135deg, var(--panel-light), var(--panel-shade) 60%, var(--panel-light));
  }
  .fruit-photo {
    position: absolute;
    left: 0;
    top: 0;
    width: 380px;
    height: 394px;
    background: linear-gradient(100deg, var(--fruit-gold) 0%, #ee8f3a 40%, var(--fruit-red) 75%, rgba(216,53,44,0) 100%);
  }
  .banner {
    position: absolute;
    left: -12px;
    top: -12px;
    width: 654px;
    height: 110px;
  }
  .banner-title {
    position: absolute;
    left: 14px;
    top: 15px;
    margin: 0;
    font-family: "Cinzel", serif;
    font-weight: 900;
    font-size: 19px;
    letter-spacing: 0.5px;
    color: var(--white);
    white-space: nowrap;
  }
  .org-mark {
    position: absolute;
    left: 429px;
    top: 18px;
    display: flex;
    align-items: center;
    gap: 8px;
  }
  .org-mark__dot {
    width: 44px;
    height: 44px;
    border-radius: 50%;
    background: var(--banner-red);
  }
  .org-mark__name {
    font-family: "Montserrat", sans-serif;
    font-weight: 800;
    font-size: 13px;
    line-height: 14px;
    color: var(--leaf-green);
  }
  .tagline {
    position: absolute;
    left: 380px;
    width: 236px;
    font-family: "Yellowtail", cursive;
    white-space: nowrap;
  }
  .pos-card--promo .tagline { top: 92px; }
  .pos-card--price .tagline { top: 122px; }
  .tagline__taste {
    font-size: 44px;
    line-height: 46px;
    color: var(--leaf-green);
  }
  .tagline__the {
    font-size: 24px;
    color: var(--accent-orange);
    margin-left: 6px;
  }
  .tagline__difference {
    position: relative;
    display: inline-block;
    margin-left: 8px;
    font-size: 44px;
    line-height: 50px;
    color: var(--script-red);
  }
  .tagline__difference::before {
    content: "";
    position: absolute;
    left: -8px;
    right: -4px;
    top: 18px;
    height: 22px;
    background: linear-gradient(90deg, rgba(240,160,32,0.2), rgba(240,160,32,0.85) 30%, rgba(240,160,32,0.6));
  }
  .tagline__difference span { position: relative; }
  .selling-points {
    position: absolute;
    margin: 0;
    padding: 0;
    list-style: none;
    font-family: "Montserrat", sans-serif;
    font-weight: 800;
    color: var(--leaf-green);
    white-space: nowrap;
  }
  .selling-points li::before {
    content: "•";
    margin-right: 3px;
  }
  .pos-card--promo .selling-points {
    left: 386px;
    top: 206px;
    font-size: 21px;
    line-height: 28px;
  }
  .pos-card--price .selling-points {
    left: 384px;
    top: 262px;
    font-size: 24px;
    line-height: 31px;
  }
  .pos-card--price .selling-points li::before {
    color: var(--accent-orange);
    margin-right: 6px;
  }
  .price-box {
    position: absolute;
    left: 388px;
    top: 298px;
    width: 228px;
    height: 84px;
    background: var(--white);
  }
</style>
</head>
<body>
<main class="sheet">

  <section class="pos-card pos-card--promo">
    <div class="card-face">
      <div class="fruit-photo" role="img" aria-label="Photo of a halved Washington peach showing its stone beside a whole ripe peach"></div>
      <svg class="banner" viewBox="0 0 654 110" aria-hidden="true">
        <polygon points="12,12 452,12 391,84 12,60" fill="var(--banner-red)"/>
        <polygon points="300,80 391,90 440,38 388,84" fill="var(--leaf-green)"/>
      </svg>
      <h1 class="banner-title">Washington State Peaches</h1>
      <div class="org-mark">
        <span class="org-mark__dot"></span>
        <span class="org-mark__name">Cascade Orchard<br>Council</span>
      </div>
      <div class="tagline">
        <div><span class="tagline__taste">Taste</span><span class="tagline__the">the</span></div>
        <div class="tagline__difference"><span>Difference!</span></div>
      </div>
      <ul class="selling-points">
        <li>New Crop!</li>
        <li>Tree Ripened</li>
        <li>Excellent Flavor</li>
      </ul>
      <div class="price-box" aria-label="Space for handwritten sale price"></div>
    </div>
  </section>

  <section class="pos-card pos-card--price">
    <div class="card-face">
      <div class="fruit-photo" role="img" aria-label="Photo of a halved Washington peach showing its stone beside a whole ripe peach"></div>
      <svg class="banner" viewBox="0 0 654 110" aria-hidden="true">
        <polygon points="12,12 452,12 391,84 12,60" fill="var(--banner-red)"/>
        <polygon points="300,80 391,90 440,38 388,84" fill="var(--leaf-green)"/>
      </svg>
      <h1 class="banner-title">Washington State Peaches</h1>
      <div class="org-mark">
        <span class="org-mark__dot"></span>
        <span class="org-mark__name">Cascade Orchard<br>Council</span>
      </div>
      <div class="tagline">
        <div><span class="tagline__taste">Taste</span><span class="tagline__the">the</span></div>
        <div class="tagline__difference"><span>Difference!</span></div>
      </div>
      <ul class="selling-points">
        <li>New Crop!</li>
        <li>Tree Ripened</li>
        <li>Excellent Flavor</li>
      </ul>
    </div>
  </section>

</main>
</body>
</html>
```